Brightfield Co Trade Show Flyer

We need a brochure design (8.5 x 11) Info in the design (refer to rough draft I drew on Paper): "#1 selling tool to aquire new franchisees has been video testimonials" - Martin L. Crowe, C.E.O Tovik Smoothie Franchise Testimonials - Let your franchisees do the selling for you. Franchisee testimonial: $10,000 / per Franchisee Includes: • 2 minute Video • 1 minute add for your franchise's location • Concept creation • Communication with franchisee • Travel to their location • All rental equipment • 1 round of corrections • Animated logo • Licensed music ******* For 25% Discount section (next to middle box), please put the "Outlet Summit Logo" Great to use on all your social media (USE logos and icons) • Website • Video • Network • Social • Photo • Posts • Phone calls • Emails • In person meetings Some of our clients: (use the logos I uploaded - in round boxes as in draft) LOGO (Brightfield Franchise Testimonial) www.brightfieldvoices.example (866) 555-0172

Target Market(s)

Franchise owners

Colors

Designer to choose colors to be used in the design.

Requirements

```html
<!DOCTYPE html>
<html lang="en">
<head>
<meta charset="utf-8">
<title>Brightfield Co – Franchisees Testimonials Flyer</title>
<link href="https://fonts.googleapis.com/css2?family=Bungee+Inline&family=Montserrat:wght@300;400;600&family=Archivo+Black&family=Oswald:wght@700&display=swap" rel="stylesheet">
<style>
  :root{
    --bg:#2e2e2f;
    --bg-glow:#3c3c3d;
    --yellow:#fff200;
    --orange:#f7941d;
    --red:#ed1c24;
    --white:#ffffff;
    --ink:#1f1f20;
  }
  *{margin:0;padding:0;box-sizing:border-box;}
  html,body{width:849px;height:1200px;overflow:hidden;background:var(--bg);}
  .flyer{
    position:relative;width:849px;height:1200px;overflow:hidden;
    background:
      radial-gradient(circle at 120px 180px, var(--bg-glow) 0, transparent 70px),
      radial-gradient(circle at 700px 120px, var(--bg-glow) 0, transparent 60px),
      radial-gradient(circle at 620px 470px, var(--bg-glow) 0, transparent 50px),
      radial-gradient(circle at 760px 390px, var(--bg-glow) 0, transparent 45px),
      radial-gradient(circle at 90px 1080px, var(--bg-glow) 0, transparent 80px),
      radial-gradient(circle at 780px 1120px, var(--bg-glow) 0, transparent 70px),
      var(--bg);
    font-family:'Montserrat',sans-serif;color:var(--white);
  }
  .quote{position:absolute;left:0;width:849px;top:22px;text-align:center;font-size:12.5px;letter-spacing:3.4px;}
  .quote-author{position:absolute;right:30px;top:48px;font-family:Arial,sans-serif;font-size:14px;}
  .headline{position:absolute;left:0;top:100px;width:849px;height:200px;}
  .headline text{font-family:'Bungee Inline',sans-serif;fill:var(--yellow);}
  .tagline{position:absolute;right:43px;top:296px;font-size:28.5px;font-weight:300;letter-spacing:.3px;}
  .burst{position:absolute;left:0;top:345px;width:290px;height:290px;}
  .burst-text{position:absolute;left:0;top:398px;width:278px;text-align:center;}
  .burst-pct{font-family:'Archivo Black',sans-serif;color:var(--yellow);font-size:44px;line-height:1;}
  .burst-label{font-family:'Archivo Black',sans-serif;color:var(--yellow);font-size:22px;line-height:1.2;}
  .burst-for{font-size:26px;color:var(--yellow);letter-spacing:8px;line-height:1.1;font-weight:400;}
  .burst-brand{font-family:'Archivo Black',sans-serif;font-size:19px;margin-top:26px;line-height:1;}
  .burst-sub{font-size:5.5px;font-weight:600;letter-spacing:.3px;}
  .package{position:absolute;left:287px;top:366px;width:550px;height:266px;border:1.5px solid var(--red);}
  .package-list{position:absolute;left:330px;top:351px;list-style:none;}
  .package-list li{display:flex;align-items:center;height:30px;color:var(--orange);font-size:20.5px;font-weight:400;background:var(--bg);padding-right:6px;}
  .package-list li:not(:first-child){background:transparent;}
  .package-list svg{width:22px;height:22px;margin-right:16px;flex:none;}
  .channels{position:absolute;top:676px;left:0;width:849px;height:44px;}
  .channel{position:absolute;top:0;width:43px;height:43px;border-radius:50%;background:var(--white);box-shadow:6px 6px 8px rgba(0,0,0,.45);display:flex;align-items:center;justify-content:center;}
  .channel span{font-size:7.5px;font-weight:600;color:var(--ink);}
  .channel svg{width:22px;height:22px;}
  .trusted{position:absolute;left:239px;top:746px;width:371px;height:42px;background:var(--red);display:flex;align-items:center;justify-content:center;gap:18px;font-size:35px;letter-spacing:1.5px;font-weight:400;}
  .trusted i{width:22px;height:22px;border:2px solid var(--white);border-radius:50%;}
  .client{position:absolute;top:799px;width:75px;height:75px;border-radius:50%;background:var(--white);box-shadow:0 0 0 2px #d9d9d9;display:flex;align-items:center;justify-content:center;text-align:center;font-size:10px;font-weight:600;color:var(--ink);}
  .divider{position:absolute;left:0;top:883px;width:849px;height:4px;background:var(--red);}
  .brand-circle{position:absolute;left:377px;top:902px;width:95px;height:95px;border-radius:50%;background:var(--white);}
  .brand-name{position:absolute;left:0;width:849px;top:1026px;text-align:center;font-family:'Archivo Black',sans-serif;font-size:60px;line-height:1;letter-spacing:1px;}
  .brand-sub{position:absolute;left:0;width:849px;top:1094px;text-align:center;font-size:18px;font-weight:600;}
  .website{position:absolute;left:0;width:849px;top:1116px;text-align:center;color:var(--yellow);font-size:28px;font-weight:400;}
  .phone{position:absolute;left:0;width:849px;top:1146px;text-align:center;color:var(--yellow);font-family:'Oswald',sans-serif;font-size:44px;line-height:1;letter-spacing:2px;}
</style>
</head>
<body>
<main class="flyer">
  <p class="quote">"#1 SELLING TOOL TO AQUIRE NEW FRANCHISEES HAS BEEN VIDEO TESTIMONIALS"</p>
  <p class="quote-author">- Martin L. Crowe, C.E.O Tovik Smoothie</p>

  <svg class="headline" viewBox="0 0 849 200" aria-label="Franchisees Testimonials">
    <text x="86" y="93" font-size="104" textLength="709" lengthAdjust="spacingAndGlyphs">FRANCHISEES</text>
    <text x="84" y="192" font-size="104" textLength="721" lengthAdjust="spacingAndGlyphs">TESTIMONIALS</text>
  </svg>
  <p class="tagline">Let your FRANCHISEES do the selling for you.</p>

  <svg class="burst" viewBox="0 0 290 290">
    <g stroke="var(--red)" stroke-width="1.2">
      <line x1="25" y1="6" x2="55" y2="48"/><line x1="5" y1="30" x2="38" y2="56"/>
      <line x1="258" y1="6" x2="232" y2="44"/><line x1="280" y1="22" x2="245" y2="50"/>
      <line x1="0" y1="62" x2="35" y2="78"/><line x1="285" y1="48" x2="252" y2="62"/>
      <line x1="0" y1="230" x2="35" y2="212"/><line x1="285" y1="226" x2="252" y2="210"/>
      <line x1="22" y1="275" x2="52" y2="235"/><line x1="260" y1="275" x2="232" y2="238"/>
      <line x1="2" y1="250" x2="38" y2="224"/><line x1="283" y1="252" x2="248" y2="228"/>
    </g>
    <g fill="var(--white)">
      <circle cx="60" cy="26" r="5"/><circle cx="155" cy="8" r="1.5"/><circle cx="219" cy="34" r="3"/>
      <circle cx="4" cy="68" r="4.5"/><circle cx="9" cy="85" r="2.5"/><circle cx="280" cy="90" r="2.5"/><circle cx="259" cy="84" r="1.5"/>
      <circle cx="6" cy="206" r="2.5"/><circle cx="22" cy="203" r="2.5"/><circle cx="258" cy="202" r="2.5"/><circle cx="278" cy="206" r="2"/>
      <circle cx="217" cy="258" r="5"/><circle cx="118" cy="276" r="3"/><circle cx="61" cy="256" r="1.5"/><circle cx="50" cy="285" r="1.5"/>
    </g>
    <polygon fill="var(--red)" stroke="var(--red)" stroke-width="2" points="139,10 160,45 190,25 196,66 232,60 220,98 258,108 230,132 262,158 226,170 246,206 206,206 210,246 174,232 162,270 139,240 116,270 104,232 68,246 72,206 32,206 52,170 16,158 48,132 20,108 58,98 46,60 82,66 88,25 118,45"/>
    <polygon fill="none" stroke="var(--ink)" stroke-width="1.3" points="139,22 158,54 186,36 191,73 224,68 213,102 248,111 222,133 251,157 218,168 236,200 200,200 203,236 171,223 160,258 139,230 118,258 107,223 75,236 78,200 42,200 60,168 27,157 56,133 30,111 65,102 54,68 87,73 92,36 120,54"/>
  </svg>
  <div class="burst-text">
    <div class="burst-pct">25%</div>
    <div class="burst-label">DISCOUNT</div>
    <div class="burst-for">FOR</div>
    <div class="burst-brand">BRIGHTFIELD</div>
    <div class="burst-sub">– FRANCHISE TESTIMONIALS –</div>
  </div>

  <div class="package"></div>
  <ul class="package-list">
    <li><svg viewBox="0 0 22 22"><circle cx="10" cy="12" r="9" fill="none" stroke="var(--orange)" stroke-width="1.4"/><path d="M5 12l4 4 10-14" fill="none" stroke="var(--orange)" stroke-width="1.6"/></svg>$10,000 / per Franchisee Includes</li>
    <li><svg viewBox="0 0 22 22"><circle cx="10" cy="12" r="9" fill="none" stroke="var(--orange)" stroke-width="1.4"/><path d="M5 12l4 4 10-14" fill="none" stroke="var(--orange)" stroke-width="1.6"/></svg>minute Video</li>
    <li><svg viewBox="0 0 22 22"><circle cx="10" cy="12" r="9" fill="none" stroke="var(--orange)" stroke-width="1.4"/><path d="M5 12l4 4 10-14" fill="none" stroke="var(--orange)" stroke-width="1.6"/></svg>1 minute add for your franchise's location</li>
    <li><svg viewBox="0 0 22 22"><circle cx="10" cy="12" r="9" fill="none" stroke="var(--orange)" stroke-width="1.4"/><path d="M5 12l4 4 10-14" fill="none" stroke="var(--orange)" stroke-width="1.6"/></svg>Concept creation</li>
    <li><svg viewBox="0 0 22 22"><circle cx="10" cy="12" r="9" fill="none" stroke="var(--orange)" stroke-width="1.4"/><path d="M5 12l4 4 10-14" fill="none" stroke="var(--orange)" stroke-width="1.6"/></svg>Communication with franchisee</li>
    <li><svg viewBox="0 0 22 22"><circle cx="10" cy="12" r="9" fill="none" stroke="var(--orange)" stroke-width="1.4"/><path d="M5 12l4 4 10-14" fill="none" stroke="var(--orange)" stroke-width="1.6"/></svg>Travel to their location</li>
    <li><svg viewBox="0 0 22 22"><circle cx="10" cy="12" r="9" fill="none" stroke="var(--orange)" stroke-width="1.4"/><path d="M5 12l4 4 10-14" fill="none" stroke="var(--orange)" stroke-width="1.6"/></svg>All rental equipment</li>
    <li><svg viewBox="0 0 22 22"><circle cx="10" cy="12" r="9" fill="none" stroke="var(--orange)" stroke-width="1.4"/><path d="M5 12l4 4 10-14" fill="none" stroke="var(--orange)" stroke-width="1.6"/></svg>1 round of corrections</li>
    <li><svg viewBox="0 0 22 22"><circle cx="10" cy="12" r="9" fill="none" stroke="var(--orange)" stroke-width="1.4"/><path d="M5 12l4 4 10-14" fill="none" stroke="var(--orange)" stroke-width="1.6"/></svg>Animated logo</li>
  </ul>

  <div class="channels">
    <div class="channel" style="left:36px"><svg viewBox="0 0 22 22" fill="none" stroke="#6a3d9a" stroke-width="1.5"><circle cx="11" cy="11" r="9"/><ellipse cx="11" cy="11" rx="4" ry="9"/><line x1="2" y1="11" x2="20" y2="11"/></svg></div>
    <div class="channel" style="left:141px"><span>Video</span></div>
    <div class="channel" style="left:245px"><span>Network</span></div>
    <div class="channel" style="left:350px"><span>Social</span></div>
    <div class="channel" style="left:454px"><span>Photo</span></div>
    <div class="channel" style="left:559px"><span>Posts</span></div>
    <div class="channel" style="left:663px"><svg viewBox="0 0 22 22"><path d="M6 3l3 4-2 2c1 3 3 5 6 6l2-2 4 3-2 3C10 19 3 12 3 5z" fill="var(--ink)"/></svg></div>
    <div class="channel" style="left:768px"><svg viewBox="0 0 22 22" fill="none" stroke="var(--red)" stroke-width="1.6"><rect x="2" y="5" width="18" height="12" rx="1"/><path d="M2 5l9 7 9-7"/></svg></div>
  </div>

  <div class="trusted"><i></i>TRUSTED BY<i></i></div>
  <div class="client" style="left:47px">Scoopline</div>
  <div class="client" style="left:185px">Corner Nine</div>
  <div class="client" style="left:323px">Axlecare</div>
  <div class="client" style="left:460px">Tovik Smoothie</div>
  <div class="client" style="left:599px">Outlet Summit</div>
  <div class="client" style="left:737px">Tidewell</div>

  <div class="divider"></div>
  <div class="brand-circle"></div>
  <p class="brand-name">BRIGHTFIELD</p>
  <p class="brand-sub">– FRANCHISE TESTIMONIALS –</p>
  <p class="website">www.brightfieldvoices.example</p>
  <p class="phone">(866) 555-0172</p>
</main>
</body>
</html>
```